Business Card Design Project

I am looking for a classy business card design for a product design consultancy. We specialize in Product Design, Prototyping, and Manufacturing Consulting. Products that we design range from consumer electronics to household products all the way to sporting goods. We are based in Arizona and called "Heron Design Works." We like to have fun and goof off as much as we like to create new products. We are young and energetic so we would like our business cards to reflect that. We already have a logo that we would like to implement into the card design. A plain rectangular business card is boring so feel free to get creative, but please, no avocado shaped cards (it's far too literal). Also feel free to play around with textured card stocks or plastic. The final design that we choose will pay attention to all of the little details. Our cards will need to be 2 sided. We're giving you guys free reign to design as you would like. Please have fun with this, it will reflect in our business card.

Thanks guys,
Heron Design Works Team

Industry/Entity Type

Electronics

Requirements
Must have
• We would like to have a spot UV coating somewhere on the business card design if possible.
Nice to have
• Let's see some designs with custom shapes rather than typical rectangular business cards but please no avocado shaped cards, thanks. Also play around with textured card socks.

```html
<!DOCTYPE html>
<html lang="en">
<head>
<meta charset="utf-8">
<title>Heron Design Works – Business Card</title>
<link rel="stylesheet" href="https://fonts.googleapis.com/css2?family=Lato:wght@400&display=swap">
<style>
  :root {
    --backdrop: #2e2e2e;
    --leaf: #92c045;
    --leaf-deep: #6f9e2a;
    --leaf-light: #b9e075;
    --paper: #ffffff;
    --ink: #222222;
    --shadow: rgba(0, 0, 0, 0.45);
  }
  * { box-sizing: border-box; margin: 0; padding: 0; }
  html, body {
    width: 1200px;
    height: 900px;
    overflow: hidden;
    background: var(--backdrop);
    font-family: "Lato", "Helvetica Neue", Arial, sans-serif;
  }
  .canvas {
    position: relative;
    width: 1200px;
    height: 900px;
  }
  .card {
    position: absolute;
    top: 301px;
    width: 513px;
    height: 296px;
    overflow: hidden;
    box-shadow: 0 6px 14px var(--shadow);
  }

  /* Front side */
  .card--front {
    left: 73px;
    background: var(--leaf);
    border-top-right-radius: 120px 130px;
  }
  .front-decoration {
    position: absolute;
    left: 0;
    top: 0;
    width: 225px;
    height: 296px;
  }
  .front-name {
    position: absolute;
    right: 34px;
    top: 150px;
    color: var(--paper);
    font-size: 27px;
    font-weight: 400;
    line-height: 32px;
    white-space: nowrap;
  }
  .services {
    position: absolute;
    left: 258px;
    top: 208px;
    list-style: none;
    color: var(--paper);
    font-size: 11.5px;
    line-height: 18px;
    letter-spacing: 0.2px;
  }
  .services li { display: flex; align-items: center; }
  .services .dot {
    width: 7px;
    height: 7px;
    border-radius: 50%;
    background: var(--paper);
    margin-right: 6px;
  }

  /* Back side */
  .card--back {
    left: 616px;
    background: var(--paper);
    border-top-left-radius: 120px 130px;
  }
  .back-name {
    position: absolute;
    right: 35px;
    top: 56px;
    display: flex;
    align-items: center;
    color: var(--leaf);
    font-size: 27px;
    font-weight: 400;
    line-height: 32px;
    white-space: nowrap;
  }
  .back-name .name-mark {
    width: 30px;
    height: 30px;
    border-radius: 50%;
    background: var(--leaf);
    margin-right: 12px;
  }
  .person {
    position: absolute;
    left: 50px;
    top: 190px;
  }
  .person-name {
    color: var(--leaf);
    font-size: 21px;
    font-weight: 400;
    line-height: 24px;
  }
  .person-role {
    color: var(--ink);
    font-size: 13px;
    letter-spacing: 0.3px;
  }
  .phones {
    position: absolute;
    left: 50px;
    top: 245px;
    color: var(--ink);
    font-size: 12.5px;
    line-height: 15px;
  }
  .address, .web {
    position: absolute;
    right: 47px;
    text-align: right;
    color: var(--ink);
    font-size: 12.5px;
    line-height: 15px;
    font-style: normal;
  }
  .address { top: 192px; }
  .web { top: 245px; }
</style>
</head>
<body>
<main class="canvas">

  <section class="card card--front" aria-label="Front of business card">
    <svg class="front-decoration" viewBox="0 0 225 296" role="img" aria-label="Decorative glossy green shape with spot UV finish">
      <defs>
        <linearGradient id="frontSheen" x1="0" y1="0" x2="1" y2="0">
          <stop offset="0" stop-color="#7aaa32"/>
          <stop offset="0.55" stop-color="#6f9e2a"/>
          <stop offset="0.75" stop-color="#b9e075"/>
          <stop offset="1" stop-color="#92c045"/>
        </linearGradient>
      </defs>
      <rect width="225" height="296" fill="url(#frontSheen)"/>
    </svg>

    <p class="front-name">Heron Design Works</p>

    <ul class="services">
      <li><span class="dot"></span>PRODUCT DESIGN</li>
      <li><span class="dot"></span>PROTOTYPING</li>
      <li><span class="dot"></span>MANUFACTURING CONSULTING</li>
    </ul>
  </section>

  <section class="card card--back" aria-label="Back of business card">
    <p class="back-name"><span class="name-mark"></span>Heron Design Works</p>

    <div class="person">
      <p class="person-name">DANIEL MARLOWE</p>
      <p class="person-role">MANAGING DIRECTOR</p>
    </div>

    <p class="phones">602 555 01 48<br>480 555 02 73</p>

    <address class="address">2140 Mesa Ridge Road<br>Tempe, Arizona 85281</address>

    <p class="web">hello@herondw.com<br>www.herondw.com</p>
  </section>

</main>
</body>
</html>
```